modern, IT themed business card for IT accelerator

Design a business card for tech oriented business accelerator. Prevailing color shall be orange.
we are operating in emerging markets and our mission is to provide co-working space, mentorship/coaching and ultimately seed financing IT startups.
also, we are helping financed ITs in obtaining next round financing, and to this end we are meeting with non IT/finance people and investment professionals..
that means card shall be designed to "impress" not only IT people (mostly liberal) but finance (more conservative)

Industry/Entity Type

Investment

Contact Information for Business Card

Company Name: Pelor Founders Yard
Name: Temur Kobaladze
Position: Partner
Address: 14, N Abashidze St., Tbilisi 0162, Georgia
Tel: +995599438165
Email: t.kobaladze@pelorhub.ge
Website: www.pelorhub.ge

Font styles to use
Sans Serif

Requirements
Must have
• Attached are logos of the company (portrait & landscape) choose any
Nice to have
• industry is IT and finance (in fact, financing IT startups). therefore design might have IT theme (inspiration from web or software designs)

```html
<!DOCTYPE html>
<html lang="en">
<head>
<meta charset="utf-8">
<title>Pelor Founders Yard — Business Card</title>
<link rel="stylesheet" href="https://fonts.googleapis.com/css2?family=Fira+Sans:ital,wght@0,400;0,600;1,400&display=swap">
<style>
  :root {
    --bg: #ececec;
    --orange-light: #e6b78b;
    --orange-mid: #dc9a5a;
    --orange-deep: #d3822f;
    --mark-grey: #8e9096;
    --mark-fill: #f1efec;
    --ink-white: #ffffff;
    --ink-grey: #8a8a90;
  }
  * { box-sizing: border-box; margin: 0; padding: 0; }
  html, body {
    width: 1200px; height: 720px; overflow: hidden;
    background: var(--bg);
    font-family: "Fira Sans", Arial, sans-serif;
  }
  .canvas {
    position: relative; width: 1200px; height: 720px;
    display: flex; align-items: center; justify-content: center; gap: 60px;
  }
  .card {
    position: relative; width: 520px; height: 300px;
    border-radius: 3px;
    box-shadow: 0 10px 28px rgba(0,0,0,.12), 0 2px 4px rgba(0,0,0,.08);
    overflow: hidden;
  }
  .card--front {
    background: linear-gradient(180deg, var(--orange-light) 0%, var(--orange-mid) 100%);
    display: flex; flex-direction: column; align-items: center; justify-content: center; gap: 18px;
  }
  .card--back {
    background: linear-gradient(200deg, var(--orange-mid) 0%, var(--orange-deep) 100%);
  }
  .brand-dot {
    width: 110px; height: 110px; border-radius: 50%;
    background: var(--mark-fill);
  }
  .brand-name {
    color: var(--mark-grey); font-weight: 600;
    font-size: 26px; letter-spacing: 2px; text-transform: uppercase; text-align: center;
    line-height: 1.1;
  }
  .card--back .brand {
    position: absolute; left: 34px; top: 74px; width: 180px;
    display: flex; flex-direction: column; align-items: center; gap: 14px;
  }
  .card--back .brand-dot { width: 100px; height: 100px; }
  .card--back .brand-name { font-size: 19px; letter-spacing: 1.5px; }
  .holder {
    position: absolute; left: 240px; top: 34px;
  }
  .holder-name {
    color: var(--ink-white); font-weight: 600; font-size: 25px;
    letter-spacing: 1.5px; text-transform: uppercase;
  }
  .holder-role {
    color: var(--ink-grey); font-style: italic; font-size: 17px; margin-top: 2px; margin-left: 26px;
  }
  .address {
    position: absolute; left: 300px; top: 118px;
    color: var(--ink-grey); font-size: 17px; line-height: 1.4; font-style: normal;
  }
  .contacts {
    position: absolute; left: 262px; top: 210px; list-style: none;
    color: var(--ink-white); font-size: 15px;
  }
  .contacts li { display: flex; align-items: center; gap: 8px; height: 24px; }
  .contacts svg { width: 16px; height: 16px; flex: none; }
  .contacts .sep { color: var(--ink-grey); }
</style>
</head>
<body>
<main class="canvas">
  <section class="card card--front" aria-label="Card front">
    <div class="brand-dot"></div>
    <div class="brand-name">Pelor<br>Founders Yard</div>
  </section>

  <section class="card card--back" aria-label="Card back">
    <div class="brand">
      <div class="brand-dot"></div>
      <div class="brand-name">Pelor<br>Founders Yard</div>
    </div>

    <div class="holder">
      <h1 class="holder-name">Temur Kobaladze</h1>
      <p class="holder-role">Partner</p>
    </div>

    <address class="address">
      14, N Abashidze St.,<br>
      Tbilisi 0162,<br>
      Georgia
    </address>

    <ul class="contacts">
      <li>
        <svg viewBox="0 0 16 16" fill="none" stroke="#fff" stroke-width="1.2"><circle cx="8" cy="8" r="7"/><path d="M5.5 4.5l1.5 0 .7 1.8-1 .8a5 5 0 0 0 2.2 2.2l.8-1 1.8.7 0 1.5c-3.5.4-6.4-2.5-6-6z" fill="#fff" stroke="none"/></svg>
        <span class="sep">|</span> +995599438165
      </li>
      <li>
        <svg viewBox="0 0 16 16" fill="none" stroke="#fff" stroke-width="1.2"><rect x="2" y="4" width="12" height="8" rx="1"/><path d="M2.5 4.5L8 9l5.5-4.5"/></svg>
        <span class="sep">|</span> t.kobaladze@pelorhub.ge
      </li>
      <li>
        <svg viewBox="0 0 16 16" fill="none" stroke="#fff" stroke-width="1.2"><circle cx="8" cy="8" r="6.5"/><ellipse cx="8" cy="8" rx="2.8" ry="6.5"/><path d="M1.5 8h13"/></svg>
        <span class="sep">|</span> www.pelorhub.ge
      </li>
    </ul>
  </section>
</main>
</body>
</html>
```